Business Card for Consulting Company

I would need a business card for my consulting company - the company brand and logos are defined and shared as part of this project. The proposed design for the business card can be reused as inspiration for my email signature.

```html
<!DOCTYPE html>
<html lang="en">
<head>
<meta charset="utf-8">
<title>Business Card – Orbiton</title>
<link href="https://fonts.googleapis.com/css2?family=Montserrat:wght@700&family=Open+Sans:wght@400;600&display=swap" rel="stylesheet">
<style>
  :root {
    --teal: #19adad;
    --teal-dark: #12807f;
    --ink: #333638;
    --rule: #8a8a8a;
    --paper: #ffffff;
    --backdrop: #d6d6d6;
  }
  * { margin: 0; padding: 0; box-sizing: border-box; }
  html, body { width: 1200px; height: 788px; overflow: hidden; }
  body {
    background: var(--backdrop);
    font-family: "Open Sans", Arial, sans-serif;
    position: relative;
  }
  .card {
    position: absolute;
    top: 244px;
    width: 510px;
    height: 300px;
    border-radius: 22px;
    box-shadow: 0 8px 24px rgba(0,0,0,0.18);
    overflow: hidden;
  }
  .card--front { left: 60px; background: var(--paper); }
  .card--back  { left: 630px; background: var(--teal); }

  .brand {
    position: absolute;
    left: 40px;
    top: 0;
    height: 100%;
    width: 190px;
    display: flex;
    align-items: center;
    gap: 10px;
  }
  .brand__dot {
    width: 22px; height: 22px;
    border-radius: 50%;
    background: var(--teal);
    flex: none;
  }
  .brand__name {
    font-weight: 600;
    font-size: 34px;
    color: var(--teal);
    letter-spacing: 0.5px;
  }
  .divider {
    position: absolute;
    left: 245px;
    top: 90px;
    width: 1px;
    height: 120px;
    background: var(--rule);
  }
  .contact {
    position: absolute;
    left: 268px;
    top: 82px;
    color: var(--ink);
  }
  .contact__name {
    font-family: "Montserrat", Arial, sans-serif;
    font-weight: 700;
    font-size: 22px;
    color: var(--teal);
    letter-spacing: 0.5px;
    line-height: 1.1;
  }
  .contact__role {
    font-size: 14px;
    line-height: 1.3;
    margin-bottom: 20px;
  }
  .contact__list { list-style: none; }
  .contact__item {
    display: flex;
    align-items: center;
    gap: 8px;
    font-size: 13px;
    line-height: 1.65;
  }
  .contact__icon { width: 10px; height: 10px; flex: none; fill: var(--teal); }

  .back-mark {
    position: absolute;
    inset: 0;
    display: flex;
    align-items: center;
    justify-content: center;
    gap: 14px;
  }
  .back-mark__dot {
    width: 56px; height: 56px;
    border-radius: 50%;
    background: var(--teal-dark);
  }
  .back-mark__name {
    font-weight: 600;
    font-size: 40px;
    color: var(--teal-dark);
  }
</style>
</head>
<body>
  <section class="card card--front">
    <div class="brand">
      <span class="brand__dot"></span>
      <span class="brand__name">Orbiton</span>
    </div>
    <div class="divider"></div>
    <div class="contact">
      <h1 class="contact__name">ELRIC VANTER</h1>
      <p class="contact__role">Founder &amp; CEO</p>
      <ul class="contact__list">
        <li class="contact__item">
          <svg class="contact__icon" viewBox="0 0 10 10"><path d="M1 2c0-1 1-1.5 2-1.5l1 2-1 1c.5 1.2 1.3 2 2.5 2.5l1-1 2 1c0 1-.5 2-1.5 2C3.5 8 2 6.5 1 2z"/></svg>
          +41 79 555 01 23
        </li>
        <li class="contact__item">
          <svg class="contact__icon" viewBox="0 0 10 10"><path d="M0 2h10v6H0z M0 2l5 3.5L10 2" /></svg>
          elric.v@orbiton-advisory.ch
        </li>
        <li class="contact__item">
          <svg class="contact__icon" viewBox="0 0 10 10"><circle cx="5" cy="5" r="5"/></svg>
          www.orbiton-advisory.ch
        </li>
      </ul>
    </div>
  </section>

  <section class="card card--back">
    <div class="back-mark">
      <span class="back-mark__dot"></span>
      <span class="back-mark__name">Orbiton</span>
    </div>
  </section>
</body>
</html>
```